Fitness Studio Grand Opening Sidewalk Poster

We need a poster designed for our new fitness studio. This will fit into an A-Frame sidewalk sign. The design should follow our color scheme of orange, grey, white.

Our logo has a gradient orange that we would like to incorporate. This is a sign that people will see as they walk by or drive by so it needs to be exciting and grab their attention in a blink of an eye.

We want this sign to drive new people to check out our business.

The logo image and text logo should be used. The "Kelta Core Fitness" text can be separated from the "sun logo symbol".

sign specs are 24x36.
I uploaded a picture of the A-Frame stand, which is orange.

The sign should read:

---start of sign text----

NOW OPEN – or – GRAND OPENING (depending on the layout)

Kelta Core Fitness (company name - in the text of the logo)

*FREE introductory class
*Personalized instruction
*Body sculpting workout
*Results training
*Fun, supportive atmosphere

1-818-555-CORE
Try A Class Today!

www.KeltaCoreFitness.example

@KeltaCoreFitness
(facebook logo, twitter logo)

----- end of sign text -----

Target Market(s)

new customers - fitness enthusiasts - woman age 30-50 - men age 40-50 -

Industry/Entity Type

Training

Font styles to use
Sans Serif

Requirements
Must have
• all the text included above - logo - work mark text
• sign should incorporate the look and feel of the logo.
• please also reference our website to get a feel of the design of the company
• www.keltacorefitness.example
Nice to have
• eye catching
• text should be easy to read while driving buy or walking
Should not have
• any other color besides the colors of the logo

```html
<!DOCTYPE html>
<html lang="en">
<head>
<meta charset="utf-8">
<title>Kelta Core Fitness – Grand Opening</title>
<link rel="stylesheet" href="https://fonts.googleapis.com/css2?family=Cinzel:wght@400&family=Fira+Sans:ital,wght@0,400;1,400&display=swap">
<style>
  :root {
    --bg-dark: #454547;
    --bg-glow: #656567;
    --orange: #f5a04c;
    --orange-light: #fbb867;
    --orange-band: #f28a5c;
    --panel: #e6e7e8;
    --ink: #3a3a3c;
    --brand-grey: #a9aaac;
    --social-square: #6d6e71;
  }
  * { margin: 0; padding: 0; box-sizing: border-box; }
  html, body { width: 800px; height: 1200px; overflow: hidden; background: var(--bg-dark); }
  .poster {
    position: relative;
    width: 800px;
    height: 1200px;
    overflow: hidden;
    background: radial-gradient(ellipse 70% 40% at 50% 32%, var(--bg-glow) 0%, var(--bg-dark) 70%);
    font-family: "Fira Sans", Arial, sans-serif;
  }
  .corridor-field {
    position: absolute;
    left: 0; top: 150px;
    width: 800px; height: 444px;
    background:
      radial-gradient(ellipse 48% 45% at 50% 52%, rgba(120,120,122,0.55) 0%, rgba(120,120,122,0) 70%),
      linear-gradient(90deg, rgba(224,122,60,0.10) 0%, rgba(224,122,60,0) 30%, rgba(224,122,60,0) 70%, rgba(224,122,60,0.10) 100%);
  }
  .headline {
    position: absolute;
    left: 0; width: 800px;
    text-align: center;
    font-family: "Cinzel", Georgia, serif;
    font-weight: 400;
    color: var(--orange);
    font-size: 94px;
    line-height: 1;
    letter-spacing: 1px;
    -webkit-text-stroke: 1px #fde3c8;
  }
  .headline--top { top: 58px; }
  .headline--bottom { top: 180px; }
  .brand-mark { position: absolute; left: 357px; top: 303px; }
  .brand-name {
    position: absolute;
    left: 0; width: 800px;
    text-align: center;
    font-family: "Fira Sans", Arial, sans-serif;
    font-weight: 400;
    color: var(--brand-grey);
    line-height: 1;
  }
  .brand-name--main { top: 474px; font-size: 42px; letter-spacing: 9px; }
  .brand-name--sub { top: 534px; font-size: 24px; letter-spacing: 9px; }
  .band-rule { position: absolute; left: 0; width: 800px; height: 8px; background: var(--orange-band); }
  .band-rule--top { top: 594px; }
  .band-rule--bottom { top: 881px; }
  .benefits {
    position: absolute;
    left: 0; top: 602px;
    width: 800px; height: 279px;
    background: var(--panel);
    list-style: none;
    padding: 18px 0 0 162px;
  }
  .benefits__item {
    display: flex;
    align-items: center;
    height: 49.5px;
    font-style: italic;
    font-size: 36px;
    color: var(--ink);
    letter-spacing: 0.6px;
  }
  .benefits__tick { width: 32px; height: 32px; margin-right: 10px; flex: none; }
  .cta {
    position: absolute;
    left: 0; width: 818px;
    text-align: center;
    color: var(--orange);
    line-height: 1;
  }
  .cta--tagline { top: 928px; font-size: 37px; }
  .cta--phone { top: 985px; font-size: 41px; letter-spacing: 0.5px; }
  .contact {
    position: absolute;
    right: 58px;
    color: var(--orange);
    font-size: 27px;
    line-height: 1;
    display: flex;
    align-items: center;
  }
  .contact--web { top: 1071px; }
  .contact--social { top: 1113px; }
  .social-square {
    width: 42px; height: 42px;
    background: var(--social-square);
    border-radius: 4px;
    margin-left: 12px;
  }
  .social-square:first-of-type { margin-left: 14px; }
</style>
</head>
<body>
<div class="poster">
  <div class="corridor-field" role="img" aria-label="Decorative receding corridor of thin orange and white light lines"></div>

  <h1 class="headline headline--top">GRAND</h1>
  <div class="headline headline--bottom">OPENING</div>

  <svg class="brand-mark" width="86" height="86" viewBox="0 0 86 86" aria-hidden="true">
    <circle cx="43" cy="43" r="42" fill="var(--orange-light)"/>
  </svg>
  <div class="brand-name brand-name--main">KELTA CORE</div>
  <div class="brand-name brand-name--sub">fitness</div>

  <div class="band-rule band-rule--top"></div>
  <ul class="benefits">
    <li class="benefits__item"><svg class="benefits__tick" viewBox="0 0 32 32" aria-hidden="true"><circle cx="15" cy="17" r="12" fill="none" stroke="var(--ink)" stroke-width="2.4"/><path d="M9 16l5 6L28 4" fill="none" stroke="var(--ink)" stroke-width="2.8" stroke-linecap="round" stroke-linejoin="round"/></svg>FREE introductory class</li>
    <li class="benefits__item"><svg class="benefits__tick" viewBox="0 0 32 32" aria-hidden="true"><circle cx="15" cy="17" r="12" fill="none" stroke="var(--ink)" stroke-width="2.4"/><path d="M9 16l5 6L28 4" fill="none" stroke="var(--ink)" stroke-width="2.8" stroke-linecap="round" stroke-linejoin="round"/></svg>Personalized instruction</li>
    <li class="benefits__item"><svg class="benefits__tick" viewBox="0 0 32 32" aria-hidden="true"><circle cx="15" cy="17" r="12" fill="none" stroke="var(--ink)" stroke-width="2.4"/><path d="M9 16l5 6L28 4" fill="none" stroke="var(--ink)" stroke-width="2.8" stroke-linecap="round" stroke-linejoin="round"/></svg>Body sculpting workout</li>
    <li class="benefits__item"><svg class="benefits__tick" viewBox="0 0 32 32" aria-hidden="true"><circle cx="15" cy="17" r="12" fill="none" stroke="var(--ink)" stroke-width="2.4"/><path d="M9 16l5 6L28 4" fill="none" stroke="var(--ink)" stroke-width="2.8" stroke-linecap="round" stroke-linejoin="round"/></svg>Results training</li>
    <li class="benefits__item"><svg class="benefits__tick" viewBox="0 0 32 32" aria-hidden="true"><circle cx="15" cy="17" r="12" fill="none" stroke="var(--ink)" stroke-width="2.4"/><path d="M9 16l5 6L28 4" fill="none" stroke="var(--ink)" stroke-width="2.8" stroke-linecap="round" stroke-linejoin="round"/></svg>Fun, supportive atmosphere</li>
  </ul>
  <div class="band-rule band-rule--bottom"></div>

  <p class="cta cta--tagline">Try A Class Today!</p>
  <p class="cta cta--phone">1-818-555-CORE</p>

  <p class="contact contact--web">www.KeltaCoreFitness.example</p>
  <p class="contact contact--social">@KeltaCoreFitness<span class="social-square"></span><span class="social-square"></span></p>
</div>
</body>
</html>
```